Modern, clean and professional Wordpress design for a safety training company!

We are currently in the process of creating a new website for our business. We have hired a website developer and the main structure of our new Wordpress site is complete. We now need an overall design plan for the site. We need a very clean, professional and easy to follow website. Most of our website visitors only spend about 30-45 secs on our sites "shopping " so it is imperative that we have a strong Home Page.
Our company specializes in CPR and First Aid Certification Classes to businesses and individuals throughout Northern California. We provide these certifications two ways: ONSITE-We come to you, and HOSTED-we offer weekly classes at our 2 locations.
Our design needs to use the general green and blue colors of our logo. But we also like white.
The final design MUST communicate a legitimate, trustworthy and professional business. Our industry is VERY competitive and we need to STAND OUT.
Currently, the NEW website that we need a new design for is www.LifelineSkillsHub.com
Our old website is www.RescueCoursesValley.com and we really do like the design of this website, but we just needed a Wordpress site for SEO purposes.
These are 3 websites that we really:
http://vorlandmedix.com/
http://www.pelbrik.com/
https://www.quimby.com/
I have attached our Logo and other images if you need to use them but looking at the current two sites will be you best help.
1) Large businesses and industries that are looking for a company to provide ONSITE safety training classes at their office or place of work.
2) Individuals that need certifications for their jobs and other needs. These individuals are looking for a legitimate, trustworthy and professional environment to complete their training class.

```html
<!DOCTYPE html>
<html lang="en">
<head>
<meta charset="utf-8">
<title>Keystone Safety Institute</title>
<link rel="stylesheet" href="https://fonts.googleapis.com/css2?family=Open+Sans:wght@400;600;700;800&display=swap">
<style>
:root{
  --blue:#1d43a0;
  --blue-dark:#15337d;
  --blue-foot:#1b3c8f;
  --green:#8dbf25;
  --green-dark:#74a316;
  --ink:#333;
  --muted:#777;
  --line:#e3e3e3;
  --white:#fff;
}
*{box-sizing:border-box;margin:0;padding:0}
html,body{width:1200px;height:2476px;overflow:hidden}
body{font-family:"Open Sans",Arial,sans-serif;color:var(--ink);background:var(--white);font-size:14px}
.wrap{width:1040px;margin:0 auto;position:relative;height:100%}

/* header */
.site-header{height:150px}
.brand{position:absolute;left:0;top:56px;display:flex;align-items:center;gap:12px}
.brand-square{width:22px;height:22px;background:var(--green)}
.brand-name{font-size:28px;font-weight:700;color:var(--blue);line-height:1;white-space:nowrap}
.header-right{position:absolute;right:0;top:22px;display:flex;gap:18px;align-items:flex-start}
.contact{text-align:right}
.socials{display:flex;gap:6px;justify-content:flex-end;margin-bottom:12px}
.socials span{width:26px;height:26px;background:var(--blue);display:block}
.contact p{color:#999;font-size:19px;line-height:1.4}
.badge{width:56px;height:86px;background:var(--blue-dark);border-radius:4px;margin-top:6px}

/* nav */
.main-nav{height:50px;background:var(--blue)}
.main-nav ul{list-style:none;display:flex;height:50px;width:1040px;margin:0 auto}
.main-nav li{color:var(--white);font-size:14px;font-weight:600;padding:0 30px;line-height:50px;border-right:1px solid rgba(255,255,255,.15)}
.main-nav li.active{background:var(--green);padding:0 40px}

/* hero */
.hero{height:560px;position:relative;background:linear-gradient(100deg,#6b8aa9 0%,#c7b5a3 35%,#9aaec7 60%,#4f6f93 100%)}
.hero-arrow{position:absolute;top:250px;width:40px;height:60px}
.hero-arrow.prev{left:6px}.hero-arrow.next{right:6px}
.dots{position:absolute;bottom:18px;left:50%;transform:translateX(-50%);display:flex;gap:8px}
.dots i{width:12px;height:12px;border-radius:50%;border:2px solid var(--white);display:block}
.dots i.on{background:var(--white)}

/* headings */
.section-title{font-size:27px;font-weight:700;color:var(--green)}
.section-title b{color:var(--blue);font-weight:700}

/* classes */
.classes{height:470px;padding-top:40px}
.class-grid{display:flex;gap:40px;margin-top:26px}
.class-card{width:320px}
.class-photo{height:170px;background:linear-gradient(135deg,#8aa0b3,#c9c2b8)}
.class-card h3{font-size:15px;font-weight:700;color:var(--ink);margin:22px 0 8px}
.class-card p{font-size:12px;color:var(--muted);line-height:1.6}
.read-more{display:inline-flex;margin-top:22px;height:34px}
.read-more span{background:var(--blue);color:var(--white);font-size:12px;padding:0 20px;line-height:34px}
.read-more em{width:34px;background:var(--green);display:flex;align-items:center;justify-content:center}

/* welcome + news */
.about{height:370px;border-top:1px solid var(--line);padding-top:40px}
.about .wrap{display:flex;gap:60px}
.welcome{width:590px}
.welcome p{font-size:12px;color:var(--muted);line-height:1.7;margin-top:18px}
.ticks{list-style:none;margin-top:12px}
.ticks li{font-size:12px;color:var(--muted);line-height:2.2;display:flex;align-items:center;gap:10px}
.ticks li::before{content:"";width:10px;height:10px;background:var(--green);border-radius:50%}
.btn-green{display:inline-block;margin-top:16px;background:var(--green);color:var(--white);font-size:11px;font-weight:700;padding:10px 18px}
.news{width:390px}
.news-item{display:flex;gap:18px;margin-top:20px}
.news-thumb{width:100px;height:90px;flex:none;background:linear-gradient(135deg,#7c93b0,#d6cdc3)}
.news-item h4{font-size:11px;font-weight:700;color:var(--ink)}
.news-item .date{font-size:11px;color:var(--green);margin:6px 0}
.news-item p{font-size:11px;color:var(--muted);line-height:1.6}

/* certifications */
.certs{height:250px;padding-top:10px}
.cert-band{display:flex;height:180px;margin-top:16px}
.cert-box{width:260px;padding:18px;color:var(--white)}
.cert-box.onsite{background:var(--blue)}
.cert-box.hosted{background:var(--green)}
.cert-box h4{font-size:14px;font-weight:700;margin-bottom:8px}
.cert-box p{font-size:11px;line-height:1.6}
.cert-photo{width:260px;background:linear-gradient(135deg,#a9b8c7,#e0dbd3)}

/* testimonials */
.testimonials{height:280px;padding-top:20px}
.quote-grid{display:flex;gap:60px;margin-top:30px}
.quote{width:490px;display:flex;gap:24px}
.avatar{width:90px;height:90px;border-radius:50%;flex:none;background:linear-gradient(135deg,#c6b4a2,#8a99ad)}
.quote h4{font-size:12px;font-weight:700;color:var(--green);margin-bottom:8px}
.quote p{font-size:11px;color:var(--muted);line-height:1.7}

/* footer */
.site-footer{height:270px;background:var(--blue-foot);color:var(--white);padding-top:36px}
.site-footer .wrap{display:flex;gap:50px}
.foot-col{width:310px}
.foot-col h5{font-size:14px;font-weight:700;margin-bottom:18px}
.foot-col p{font-size:11px;line-height:1.7;opacity:.85}
.tweet{display:flex;gap:10px;margin-bottom:14px}
.tweet::before{content:"";width:14px;height:14px;flex:none;background:var(--white);margin-top:2px}
.signup{display:flex;margin-top:18px}
.signup span{flex:1;background:var(--white);color:#aaa;font-size:11px;padding:0 12px;line-height:34px}
.signup strong{background:var(--green);font-size:12px;padding:0 16px;line-height:34px}
.bottom-bar{height:76px;background:var(--green);color:var(--white)}
.bottom-bar .wrap{display:flex;align-items:center;justify-content:space-between}
.bottom-bar p{font-size:11px;font-weight:600}
.bottom-bar .socials{margin:0}
.bottom-bar .socials span{background:var(--blue);width:30px;height:30px}
</style>
</head>
<body>

<header class="site-header">
  <div class="wrap">
    <div class="brand"><span class="brand-square"></span><span class="brand-name">Keystone Safety Institute</span></div>
    <div class="header-right">
      <div class="contact">
        <div class="socials"><span></span><span></span><span></span><span></span></div>
        <p>info@keystonesafety.com</p>
        <p>555-014-2270</p>
      </div>
      <div class="badge" role="img" aria-label="Accreditation badge"></div>
    </div>
  </div>
</header>

<nav class="main-nav">
  <ul>
    <li class="active">Home</li><li>Class Calendar</li><li>Classes for Groups</li><li>Certification Classes</li><li>About Us</li><li>Policies</li>
  </ul>
</nav>

<section class="hero" role="img" aria-label="Instructors leading a hands-on medical training session">
  <svg class="hero-arrow prev" viewBox="0 0 40 60"><path d="M28 8 8 30l20 22" fill="none" stroke="#fff" stroke-width="6"/></svg>
  <svg class="hero-arrow next" viewBox="0 0 40 60"><path d="M12 8l20 22-20 22" fill="none" stroke="#fff" stroke-width="6"/></svg>
  <div class="dots"><i></i><i class="on"></i><i></i></div>
</section>

<section class="classes">
  <div class="wrap">
    <h2 class="section-title">Our <b>Classes</b></h2>
    <div class="class-grid">
      <article class="class-card">
        <div class="class-photo" role="img" aria-label="CPR practice on a training manikin"></div>
        <h3>CPR</h3>
        <p>Learn chest compressions and rescue breathing with certified instructors in a calm, supportive, hands-on class setting for every learner.</p>
        <div class="read-more"><span>Read more</span><em><svg width="10" height="12" viewBox="0 0 10 12"><path d="M1 0l8 6-8 6z" fill="#fff"/></svg></em></div>
      </article>
      <article class="class-card">
        <div class="class-photo" role="img" aria-label="First aid bandaging practice"></div>
        <h3>FIRST AID CERTIFICATION</h3>
        <p>Gain skills for treating cuts, burns, sprains and sudden illness, and earn a recognized certification valid for two full years.</p>
        <div class="read-more"><span>Read more</span><em><svg width="10" height="12" viewBox="0 0 10 12"><path d="M1 0l8 6-8 6z" fill="#fff"/></svg></em></div>
      </article>
      <article class="class-card">
        <div class="class-photo" role="img" aria-label="Group training class in session"></div>
        <h3>TRAINING CLASSES</h3>
        <p>Weekly hosted classes at our two locations, or onsite sessions for teams at your office, plant or other place of work.</p>
        <div class="read-more"><span>Read more</span><em><svg width="10" height="12" viewBox="0 0 10 12"><path d="M1 0l8 6-8 6z" fill="#fff"/></svg></em></div>
      </article>
    </div>
  </div>
</section>

<section class="about">
  <div class="wrap">
    <div class="welcome">
      <h2 class="section-title">Welcome To <b>Keystone Safety Institute!</b></h2>
      <p>We provide CPR and First Aid certification classes to businesses and individuals throughout Northern California. Our instructors bring real field experience, clear teaching and a friendly approach, so every student leaves confident, prepared and properly certified for work and everyday life.</p>
      <ul class="ticks">
        <li>Certified instructors with field experience</li>
        <li>Small classes with hands-on practice</li>
        <li>Same day certification cards for students</li>
      </ul>
      <span class="btn-green">CLICK HERE FOR MORE INFORMATION</span>
    </div>
    <div class="news">
      <h2 class="section-title"><b>Latest</b> News</h2>
      <div class="news-item">
        <div class="news-thumb" role="img" aria-label="Students in a class"></div>
        <div><h4>NEW WEEKLY CLASS SCHEDULE POSTED</h4><div class="date">25 - FEB, 2014</div><p>Our spring calendar is live with added evening and weekend sessions at both locations.</p></div>
      </div>
      <div class="news-item">
        <div class="news-thumb" role="img" aria-label="Instructor demonstrating a technique"></div>
        <div><h4>ONSITE TRAINING FOR LARGE TEAMS</h4><div class="date">18 - FEB, 2014</div><p>Book group sessions at your workplace with flexible times to suit every shift.</p></div>
      </div>
    </div>
  </div>
</section>

<section class="certs">
  <div class="wrap">
    <h2 class="section-title"><b>Certifications</b></h2>
    <div class="cert-band">
      <div class="cert-box onsite"><h4>ONSITE-We come to you</h4><p>We bring instructors and all equipment to your office or work site for easy group training.</p></div>
      <div class="cert-photo" role="img" aria-label="Training equipment laid out in a classroom"></div>
      <div class="cert-box hosted"><h4>HOSTED-we offer</h4><p>Weekly classes at our two comfortable locations, open to individuals and small groups.</p></div>
      <div class="cert-photo" role="img" aria-label="Training manikins ready for class"></div>
    </div>
  </div>
</section>

<section class="testimonials">
  <div class="wrap">
    <h2 class="section-title"><b>Testimonials</b></h2>
    <div class="quote-grid">
      <div class="quote">
        <div class="avatar" role="img" aria-label="Portrait of a client"></div>
        <div><h4>ORGANIZATIONAL CAPACITY</h4><p>The instructor was clear, patient and engaging. Our whole staff finished certified in one morning, and everyone said it was the best training day we have had in years.</p></div>
      </div>
      <div class="quote">
        <div class="avatar" role="img" aria-label="Portrait of a client"></div>
        <div><h4>SYNERGIC NETWORK</h4><p>Booking was simple and the class was practical from start to finish. I needed a card for my new job and walked out the same day fully certified and confident.</p></div>
      </div>
    </div>
  </div>
</section>

<footer class="site-footer">
  <div class="wrap">
    <div class="foot-col"><h5>LOCATION</h5><p>Two training centers serving Northern California, with free parking, easy access and classrooms set up for hands-on practice every week.</p></div>
    <div class="foot-col"><h5>LATEST TWEETS</h5>
      <p class="tweet">New evening CPR classes added this month, reserve a seat now.</p>
      <p class="tweet">Onsite group training available for teams of any size.</p>
    </div>
    <div class="foot-col"><h5>NEWSLETTER</h5><p>Sign up for class dates, certification reminders and safety tips sent once a month.</p>
      <div class="signup"><span>Enter your email address</span><strong>Sign Up</strong></div>
    </div>
  </div>
</footer>

<div class="bottom-bar">
  <div class="wrap">
    <p>COPYRIGHT © 2014 KEYSTONE SAFETY INSTITUTE, ALL RIGHTS RESERVED</p>
    <div class="socials"><span></span><span></span><span></span><span></span></div>
  </div>
</div>

</body>
</html>
```